Tandem Tots Flyer - 2 WEEK FREE TRIAL

FLYER - We need a 1 page DL flyer with images and text. Have flyer in landscape

OFFER - 2 WEEK FREE TRIAL

HOW TO GET
Book online now at www.tandemtotsplay.com.au/booking

TAG -Where Kids are Champions

PRIZE
Chance to win Full Term of 10 weekly sessions

GIVEAWAYS
Chance to get giveaways such as tickets to games, footballs or other great offers.

LOGO - Attached

Target Market(s)

Parents of children from 5 to 16

Industry/Entity Type

Fitness

Colors
0455a3
ffc214

Requirements
Must have
• Attraction for parents to go online and sign up their kids
Should not have
• Not dull or boring

```html
<!DOCTYPE html>
<html lang="en">
<head>
<meta charset="utf-8">
<title>Tandem Tots – 2 Week Free Trial Flyer</title>
<link rel="stylesheet" href="https://fonts.googleapis.com/css2?family=Rubik+Dirt&family=Roboto+Condensed:wght@400;700&display=swap">
<style>
  :root{
    --navy:#0b2a78;
    --brand-blue:#0455a3;
    --yellow:#ffc214;
    --gold-light:#ffd24a;
    --gold-dark:#f2a50c;
    --black:#141414;
    --white:#ffffff;
    --sky-top:#7fb1dd;
    --sky-bottom:#e4eef7;
    --page:#d9d9d9;
  }
  *{margin:0;padding:0;box-sizing:border-box}
  html,body{width:1200px;height:708px;overflow:hidden;background:var(--page)}
  .flyer{position:absolute;left:50px;top:81px;width:1100px;height:546px;overflow:hidden;background:var(--navy);font-family:"Roboto Condensed",Arial,sans-serif}
  .flyer__bg{position:absolute;inset:0;width:100%;height:100%}
  .badge{position:absolute;left:88px;top:22px;width:240px;height:240px}
  .badge__text{position:absolute;inset:0;display:flex;flex-direction:column;align-items:center;justify-content:center;color:var(--navy);font-weight:700;line-height:1}
  .badge__row{display:flex;align-items:flex-end;gap:6px}
  .badge__num{font-size:86px;letter-spacing:-2px}
  .badge__unit{font-size:40px;padding-bottom:8px}
  .badge__label{font-size:38px;margin-top:2px}
  .headline{position:absolute;right:60px;top:34px;text-align:right;line-height:1;white-space:nowrap}
  .headline__top{font-family:"Rubik Dirt",Impact,sans-serif;font-size:90px;color:var(--navy);letter-spacing:1px}
  .headline__bottom{font-family:"Roboto Condensed",Arial,sans-serif;font-weight:700;font-size:72px;color:var(--black);margin-top:12px}
  .prize__lead{position:absolute;left:93px;top:258px;font-size:33px;font-weight:700;color:var(--navy);white-space:nowrap}
  .prize__box{position:absolute;left:72px;top:309px;width:556px;height:70px;background:var(--yellow);border-radius:8px;box-shadow:0 3px 6px rgba(0,0,0,.2);display:flex;align-items:center;justify-content:center;font-family:"Rubik Dirt",Impact,sans-serif;font-size:37px;color:var(--black);white-space:nowrap;overflow:hidden}
  .giveaways{position:absolute;left:82px;top:392px;font-size:16px;font-weight:700;color:var(--black);line-height:1.3;white-space:nowrap}
  .programs{position:absolute;left:452px;top:412px;display:flex;gap:14px}
  .program{display:flex;align-items:center;gap:5px;font-size:13px;font-weight:700;color:var(--navy);line-height:1.05;white-space:nowrap}
  .program__dot{width:12px;height:12px;border-radius:50%;background:var(--navy);flex:none}
  .booking{position:absolute;left:36px;top:465px;font-weight:700;white-space:nowrap}
  .booking__label{font-size:19px;color:var(--white);letter-spacing:1px;text-transform:uppercase}
  .booking__url{font-size:17px;color:var(--yellow);margin-top:8px}
</style>
</head>
<body>
<main class="flyer">
  <svg class="flyer__bg" viewBox="0 0 1100 546" preserveAspectRatio="none">
    <defs>
      <linearGradient id="skyFill" x1="0" y1="0" x2="0" y2="1">
        <stop offset="0" stop-color="var(--sky-top)"/>
        <stop offset="1" stop-color="var(--sky-bottom)"/>
      </linearGradient>
      <linearGradient id="yellowFill" x1="0" y1="0" x2="1" y2="1">
        <stop offset="0" stop-color="#ffd21e"/>
        <stop offset="1" stop-color="#f5b80c"/>
      </linearGradient>
    </defs>
    <polygon points="400,0 1100,0 1100,180 790,360 300,150" fill="url(#yellowFill)"/>
    <polygon points="0,300 300,172 800,382 640,546 0,546" fill="var(--white)"/>
    <line x1="0" y1="292" x2="300" y2="164" stroke="var(--yellow)" stroke-width="6"/>
    <polygon points="0,438 600,480 560,546 0,546" fill="var(--black)"/>
    <line x1="0" y1="434" x2="604" y2="476" stroke="var(--yellow)" stroke-width="4"/>
    <polygon points="1100,196 1100,546 640,546" fill="var(--yellow)"/>
    <g role="img" aria-label="Photo of a smiling boy in a yellow shirt balancing a soccer ball on his head against a cloudy blue sky">
      <polygon points="1100,206 1100,546 660,546" fill="url(#skyFill)"/>
    </g>
  </svg>

  <div class="badge">
    <svg viewBox="0 0 240 240" width="240" height="240">
      <defs>
        <linearGradient id="badgeFill" x1="0" y1="0" x2="0" y2="1">
          <stop offset="0" stop-color="var(--gold-light)"/>
          <stop offset="1" stop-color="var(--gold-dark)"/>
        </linearGradient>
      </defs>
      <polygon points="120,8 214,62 214,170 120,226 26,170 26,62" fill="url(#badgeFill)" stroke="var(--white)" stroke-width="8" stroke-linejoin="round"/>
    </svg>
    <div class="badge__text">
      <div class="badge__row"><span class="badge__num">2</span><span class="badge__unit">week</span></div>
      <div class="badge__label">FREE TRIAL</div>
    </div>
  </div>

  <h1 class="headline">
    <div class="headline__top">WHERE KIDS</div>
    <div class="headline__bottom">ARE CHAMPIONS</div>
  </h1>

  <p class="prize__lead">Chance to win Full Term of</p>
  <div class="prize__box">10 WEEKLY SESSIONS</div>

  <p class="giveaways">Chance to get giveaways such as tickets to games<br>footballs or other great offers.</p>

  <div class="programs">
    <div class="program"><span class="program__dot"></span><span>Tandem Tots<br>Soccer</span></div>
    <div class="program"><span class="program__dot"></span><span>Tandem Tots<br>Football</span></div>
    <div class="program"><span class="program__dot"></span><span>Tandem Tots<br>Sport</span></div>
  </div>

  <div class="booking">
    <div class="booking__label">Book online now at</div>
    <div class="booking__url">www.tandemtotsplay.com.au/booking</div>
  </div>
</main>
</body>
</html>
```